Webpage needed for a new legal recruitment/headhunting companyi

I would like a professional and sharp looking website to showcase a new legal headhunting/recruitment company called Mosswick. The logo for the company is attached.

I like the following websites:
http://www.brindletalent.co.uk/
(For the general style and layout- although photographs of the team will be difficult as we don't have one yet!;-))

http://qorv.co.uk/
I like the style of the photographs etc on this one.

NB the pictures attached below are for information only- I don't think I would be able to use any of them...

Hope you can help!
Many thanks

Industry/Entity Type

Legal

```html
<!DOCTYPE html>
<html lang="en">
<head>
<meta charset="utf-8">
<title>Mosswick Legal Recruitment</title>
<link href="https://fonts.googleapis.com/css2?family=Open+Sans:wght@300;400;700&family=Noto+Serif:ital@1&display=swap" rel="stylesheet">
<style>
:root{
  --purple:#4b2c6b;
  --purple-text:#4d3370;
  --black:#000;
  --panel:#141414;
  --white:#fff;
  --grey-text:#9a9a9a;
  --rule:#dcdcdc;
  --dark-text:#222;
}
*{box-sizing:border-box;margin:0;padding:0}
html,body{width:1200px;height:871px;overflow:hidden}
body{position:relative;background:var(--white);font-family:"Open Sans",Arial,sans-serif;color:var(--dark-text)}

.topbar{position:absolute;left:0;top:0;width:1200px;height:32px;border-bottom:1px solid var(--rule);font-size:12px;color:var(--dark-text)}
.topbar-item{position:absolute;top:9px;display:flex;align-items:center;gap:8px;line-height:14px}
.topbar-item svg{width:12px;height:12px;fill:var(--dark-text)}

.header{position:absolute;left:0;top:32px;width:1200px;height:116px}
.brand{position:absolute;left:28px;top:24px}
.brand-name{display:flex;align-items:center;gap:10px;font-size:44px;font-weight:400;color:var(--purple);letter-spacing:1px;line-height:48px}
.brand-dot{width:26px;height:26px;border-radius:50%;background:var(--purple)}
.brand-tag{position:absolute;left:120px;top:48px;font-size:13px;color:#777;white-space:nowrap}
.nav{position:absolute;left:610px;top:0;height:116px;display:flex}
.nav-link{height:116px;display:flex;align-items:center;justify-content:center;border-left:1px solid var(--rule);font-size:15px;font-weight:400;color:var(--grey-text);text-transform:uppercase}
.nav-link.is-active{color:var(--purple-text)}

.stage{position:absolute;left:0;top:148px;width:1200px;height:664px;background:var(--black)}
.hero{position:absolute;left:9px;top:23px;width:583px;height:297px;overflow:hidden}
.hero-photo{position:absolute;inset:0;background:linear-gradient(90deg,#5e5e5e 0%,#8a8a8a 22%,#555 45%,#333 75%,#2a2a2a 100%)}
.hero-copy{position:absolute;left:262px;top:26px;width:300px;text-align:center;color:var(--white)}
.hero-year{font-size:110px;font-weight:300;line-height:110px}
.hero-line{font-size:31px;font-weight:300;line-height:32px}
.hero-for{position:relative;font-family:"Noto Serif",Georgia,serif;font-style:italic;font-size:26px;line-height:40px}
.hero-for::before,.hero-for::after{content:"";position:absolute;top:21px;height:1px;width:70px;background:var(--white)}
.hero-for::before{left:2px}.hero-for::after{right:0}
.hero-big{font-size:60px;font-weight:300;line-height:64px}

.welcome{position:absolute;left:9px;top:339px;width:583px;height:295px;background:var(--panel);padding:12px 16px;color:var(--white)}
.welcome h1{font-size:35px;font-weight:300;color:var(--purple-text);line-height:38px;margin-bottom:12px}
.welcome p{font-size:15px;line-height:18px;margin-bottom:18px}

.tweets{position:absolute;left:608px;top:23px;width:282px;height:611px;background:var(--panel);padding:14px 12px;color:var(--white);overflow:hidden}
.tweets-title{display:flex;align-items:center;gap:12px;font-size:35px;font-weight:300;color:var(--purple-text);line-height:38px;margin-bottom:18px}
.tweets-mark{width:34px;height:34px;border-radius:50%;background:var(--white)}
.tweet{font-family:"Noto Serif",Georgia,serif;font-style:italic;font-size:14.5px;line-height:19px}
.tweet-sep{width:16px;margin:10px auto 8px;border-top:1px dotted var(--white)}

.cta{position:absolute;left:905px;top:23px;width:282px;height:296px;background:var(--purple);color:var(--white);text-align:center}
.cta-block{position:absolute;left:0;width:100%}
.cta-thin{font-size:40px;font-weight:300;line-height:40px}
.cta-small{font-family:"Noto Serif",Georgia,serif;font-style:italic;font-size:13px;line-height:18px}
.cta-bold{font-size:28px;font-weight:700;line-height:32px}
.cta-rule{position:absolute;left:11px;top:166px;width:262px;height:1px;background:var(--white)}

.menu{position:absolute;left:905px;top:339px;width:282px;height:295px;background:var(--panel)}
.menu-item{position:absolute;left:12px;font-size:26px;font-weight:300;color:var(--white);line-height:50px;padding:0 10px}
.menu-item.is-active{background:var(--purple);left:2px}

.footer{position:absolute;left:0;top:812px;width:1200px;height:59px;font-size:14px;color:var(--dark-text)}
.footer-mark{position:absolute;left:12px;top:12px;width:34px;height:34px;border-radius:50%;border:3px solid var(--purple)}
.footer-copy{position:absolute;left:60px;top:20px}
.footer-rule{position:absolute;left:291px;top:0;width:1px;height:59px;background:var(--rule)}
</style>
</head>
<body>

<div class="topbar">
  <div class="topbar-item" style="left:14px">
    <svg viewBox="0 0 12 12"><path d="M6 0a4 4 0 0 0-4 4c0 3 4 8 4 8s4-5 4-8a4 4 0 0 0-4-4zm0 5.6A1.6 1.6 0 1 1 6 2.4a1.6 1.6 0 0 1 0 3.2z"/></svg>
    Your Address, Harbor City, 10450 NY
  </div>
  <div class="topbar-item" style="left:276px">
    <svg viewBox="0 0 12 12"><path d="M0 2h12v8H0z M1 3l5 4 5-4" fill="none" stroke="#222" stroke-width="1.4"/></svg>
    info@mosswick.com
  </div>
  <div class="topbar-item" style="left:414px">
    <svg viewBox="0 0 12 12"><path d="M2.5 0.5l2 2.5-1.2 1.5a7 7 0 0 0 4.2 4.2L9 7.5l2.5 2-1.5 2C5 11 1 7 .5 2z"/></svg>
    (123) 123 4567
  </div>
  <div class="topbar-item" style="left:868px">
    <svg viewBox="0 0 12 12"><circle cx="6" cy="6" r="5" fill="none" stroke="#222" stroke-width="1.6"/><path d="M6 3v3.3h2.4" fill="none" stroke="#222" stroke-width="1.4"/></svg>
    When you are open timeing FRI from 7am till 11pm
  </div>
</div>

<header class="header">
  <div class="brand">
    <div class="brand-name"><span class="brand-dot"></span>MOSSWICK</div>
    <div class="brand-tag">Legal Recruitment</div>
  </div>
  <nav class="nav">
    <a class="nav-link is-active" style="width:94px">Home</a>
    <a class="nav-link" style="width:142px">Candidates</a>
    <a class="nav-link" style="width:135px">Your Team</a>
    <a class="nav-link" style="width:112px">Clients</a>
    <a class="nav-link" style="width:107px">Blogs</a>
  </nav>
</header>

<main class="stage">
  <section class="hero">
    <div class="hero-photo" role="img" aria-label="Black and white portrait photograph of a smiling consultant in a suit"></div>
    <div class="hero-copy">
      <div class="hero-year">2013</div>
      <div class="hero-line">was a record year</div>
      <div class="hero-for">/ for our /</div>
      <div class="hero-big">BUSINESS</div>
    </div>
  </section>

  <section class="welcome">
    <h1>Welcome to MOSSWICK</h1>
    <p>Mosswick is very clear about what it stands for. We are a firm of<br>headhunters servicing the legal sector. Our aim is to find our<br>clients the best lawyers in the market. They may not necessarily be the best<br>lawyers actively considering a move.</p>
    <p>We take our work and our clients seriously, but not ourselves.<br>We believe that you can be professional, creative, ethical, focused and suc-<br>cessful and still keep a smile on your face.</p>
    <p>That’s why our clients, our targets, our candidates and our<br>colleagues enjoy working with us. Feel free to ask them!</p>
  </section>

  <section class="tweets">
    <div class="tweets-title"><span class="tweets-mark"></span>Latest Tweet</div>
    <p class="tweet">Mosswick is very clear about what it stands for. We are a firm of headhunters servicing the legal sector. Our aim is to find our clients the best lawyers in the market. They may not necessarily be the best lawyers actively considering a move.</p>
    <div class="tweet-sep"></div>
    <p class="tweet">We take our work and our clients seriously, but not ourselves.<br>We believe that you can be profes-sional, creative, ethical, focused and successful and still keep a smile on your face.</p>
    <div class="tweet-sep"></div>
    <p class="tweet">That’s why our clients, our targets, our candidates and our colleagues enjoy working with us. Feel free to ask them!</p>
    <div class="tweet-sep"></div>
    <p class="tweet">We take our work and our clients seriously, but not ourselves.<br>We believe that</p>
    <div class="tweet-sep"></div>
    <p class="tweet">That’s why our clients, our targets, our candidates and our</p>
  </section>

  <section class="cta">
    <div class="cta-block" style="top:50px">
      <div class="cta-thin">CONTACT</div>
      <div class="cta-small">/ our /</div>
      <div class="cta-bold">CONSULTANT</div>
    </div>
    <div class="cta-rule"></div>
    <div class="cta-block" style="top:198px">
      <div class="cta-thin">READ OUR</div>
      <div class="cta-bold">LATEST BLOG</div>
    </div>
  </section>

  <nav class="menu">
    <a class="menu-item" style="top:15px;left:4px">What we are working</a>
    <a class="menu-item is-active" style="top:86px">Recent Successes</a>
    <a class="menu-item" style="top:153px;left:2px">Real Salaries</a>
    <a class="menu-item" style="top:221px;left:6px">Testimonials</a>
  </nav>
</main>

<footer class="footer">
  <span class="footer-mark"></span>
  <span class="footer-copy">Copyright © 2014 Mosswick.</span>
  <span class="footer-rule"></span>
</footer>

</body>
</html>
```